R.Tamo Fiji Limited

to create a master letter head with 35 years of fijian owned
Company boilerplate (for proposals/emails)
R. Tamo Fiji Limited is a respected Fijian company with 35 years of continuous service to our communities across the Pacific. We deliver end-to-end manufacturing and engineering, commercial refrigeration & air-conditioning, property development/management, and mobility solutions. As a distributor of Q-R-VU golf carts and Maplor batteries, we support resorts, airports, and industries with reliable supply, parts, and after-sales service. Built on craftsmanship, integrity, and community, R. Tamo has become a household name in Fiji.
About-us paragraph (website “About”)
For 35 years, R. Tamo Fiji Limited has been a pillar of the local economy and a trusted partner throughout the Pacific Islands. Our group combines precision manufacturing and stainless-steel fabrication with refrigeration & air-conditioning projects, real-estate development, and golf-cart fleets and energy systems. We proudly distribute Q-R-VU golf carts and Maplor batteries, and we back every sale with responsive technical support. Our promise is simple: reliable quality, fair value, and long-term support for every client.
Group Buiness

```html
<!DOCTYPE html>
<html lang="en">
<head>
<meta charset="utf-8">
<title>R.Tamo Fiji Limited — Letterhead</title>
<link rel="stylesheet" href="https://fonts.googleapis.com/css2?family=Source+Sans+3:wght@400;600&display=swap">
<style>
  :root {
    --navy: #163f73;
    --orange: #f9a825;
    --ink-soft: #5a5a5a;
    --paper: #ffffff;
    --backdrop: #a9a8a8;
    --placeholder: #f3f3f3;
  }
  * { margin: 0; padding: 0; box-sizing: border-box; }
  html, body { width: 964px; height: 1200px; overflow: hidden; }
  body {
    background: var(--backdrop);
    font-family: "Source Sans 3", sans-serif;
    color: var(--ink-soft);
  }
  .letterhead {
    position: absolute;
    left: 68px; top: 16px;
    width: 827px; height: 1168px;
    background: var(--paper);
    overflow: hidden;
  }
  .brand-name {
    position: absolute; left: 78px; top: 100px;
    font-size: 28px; font-weight: 600; color: var(--navy);
    line-height: 1;
  }
  .date {
    position: absolute; left: 80px; top: 295px;
    font-size: 15px; font-weight: 600;
  }
  .recipient {
    position: absolute; left: 80px; top: 355px;
    font-size: 15px; font-weight: 600;
    line-height: 20px; font-style: normal;
  }
  .body-copy {
    position: absolute; left: 78px; top: 470px; width: 668px;
    font-size: 13.6px; line-height: 20px;
    text-align: justify;
    hyphens: auto;
  }
  .body-copy p + p { margin-top: 20px; }
  .signature {
    position: absolute; left: 593px; top: 872px;
    width: 133px; height: 54px;
    background: var(--placeholder);
  }
  .signatory-title {
    position: absolute; left: 628px; top: 930px;
    font-size: 13px;
  }
  .contact {
    position: absolute; left: 78px; top: 1008px;
    font-size: 13px; line-height: 16px; font-style: normal;
  }
  .contact-rule { width: 50px; height: 1px; background: var(--ink-soft); margin: 12px 0; }
  .contact-line { display: flex; align-items: center; gap: 7px; height: 21px; }
  .contact-line svg { width: 16px; height: 16px; flex: none; }
  .band { position: absolute; right: 0; height: 17px; }
  .band-navy { left: 442px; top: 1077px; background: var(--navy); }
  .band-orange { left: 322px; top: 1111px; background: var(--orange); }
</style>
</head>
<body>
  <main class="letterhead">
    <header>
      <p class="brand-name">R.Tamo Fiji Limited</p>
    </header>

    <p class="date">Cartagena de Indias, Ocober 12,2015</p>

    <address class="recipient">
      Sr.<br>MARCO RUIZ<br>Web Master<br>City
    </address>

    <section class="body-copy" lang="en">
      <p>Contrary to popular belief, Lorem Ipsum is not simply random text. It has roots in a piece of classical Latin literature from 45 BC, making it over 2000 years old. Edwin Harrow, a Latin professor at Wrenfield College in Virginia, looked up one of the more obscure Latin words, consectetur, from a Lorem Ipsum passage, and going through the cites of the word in classical literature,</p>
      <p>discovered the undoubtable source. Lorem Ipsum comes from sections 1.10.32 and 1.10.33 of "de Finibus Bonorum et Malorum" (The Extremes of Good and Evil) by Marcus Tellio, written in 45 BC. This book is a treatise on the theory of ethics, very popular during the Renaissance. The first line of Lorem Ipsum, "Lorem ipsum dolor sit amet..", comes from a line in section 1.10.32.</p>
      <p>The standard chunk of Lorem Ipsum used since the 1500s is reproduced below for those interested. Sections 1.10.32 and 1.10.33 from "de Finibus Bonorum et Malorum" by Marcus Tellio are also reproduced in their exact original form, accompanied by English versions from the 1914 translation by H. Bramwell.</p>
      <p>There are many variations of passages of Lorem Ipsum available, but the majority have suffered alteration in some form, by injected humour, or randomised words which don't look even slightly believable. If you are going to use a passage of Lorem Ipsum, you need to be sure there isn't anything embarrassing hidden in the middle of text. All the Lorem Ipsum generators o</p>
    </section>

    <div class="signature" role="img" aria-label="Handwritten signature of the CEO"></div>
    <p class="signatory-title">CEO/ FOUNDER</p>

    <address class="contact">
      4810 Harbour View Rd<br>Lautoka Bay, FL 33090
      <div class="contact-rule"></div>
      <div class="contact-line">
        <svg viewBox="0 0 16 16" aria-hidden="true"><circle cx="8" cy="8" r="8" fill="#163f73"/><path d="M5.2 4.2l1.4-.3.8 2-1 .8a6 6 0 0 0 2.9 2.9l.8-1 2 .8-.3 1.4c-.2.5-.7.8-1.3.7A8 8 0 0 1 4.5 5.5c-.1-.6.2-1.1.7-1.3z" fill="#fff"/></svg>
        <span>555-014-2290</span>
      </div>
      <div class="contact-line">
        <svg viewBox="0 0 16 16" aria-hidden="true"><circle cx="8" cy="8" r="8" fill="#163f73"/><rect x="4" y="5.2" width="8" height="5.6" rx=".6" fill="#fff"/><path d="M4.3 5.6 8 8.4l3.7-2.8" fill="none" stroke="#163f73" stroke-width=".9"/></svg>
        <span>info@RTamo.com</span>
      </div>
      <div class="contact-line">
        <svg viewBox="0 0 16 16" aria-hidden="true"><circle cx="8" cy="8" r="8" fill="#163f73"/><circle cx="8" cy="8" r="4.5" fill="none" stroke="#fff" stroke-width="1"/><path d="M3.5 8h9M8 3.5c-2 2.4-2 6.6 0 9M8 3.5c2 2.4 2 6.6 0 9" fill="none" stroke="#fff" stroke-width=".9"/></svg>
        <span>www.RTamo.com</span>
      </div>
    </address>

    <div class="band band-navy"></div>
    <div class="band band-orange"></div>
  </main>
</body>
</html>
```